Design business card for Bright Harbour Coaching!

I am a personal development coach (like a life coach) and corporate trainer and need a professionally designed double sided business card.

It needs to contain the business logo (I'm happy for the designer to choose the layout of the logo as I am still working out the best option myself) and the following information:

Tamsin Varga
Personal Development Coach and Trainer

+61 (0)452 819 407 (written that way)
tamsin@bright-harbour.com

www.bright-harbour.com

```html
<!DOCTYPE html>
<html lang="en">
<head>
<meta charset="utf-8">
<title>Bright Harbour Coaching – Business Card</title>
<link rel="stylesheet" href="https://fonts.googleapis.com/css2?family=Tinos:wght@400&display=swap">
<style>
  :root {
    --backdrop: #8f8f8f;
    --card: #eeeff1;
    --teal: #0f8390;
    --teal-deep: #0b6470;
    --name: #0e6c77;
    --ink: #111111;
    --brand-grey: #58585a;
  }
  * { margin: 0; padding: 0; box-sizing: border-box; }
  html, body {
    width: 1105px;
    height: 1200px;
    overflow: hidden;
    background: var(--backdrop);
    font-family: "Tinos", "Times New Roman", serif;
  }
  .canvas {
    position: relative;
    width: 1105px;
    height: 1200px;
  }
  .card {
    position: absolute;
    left: 182px;
    width: 746px;
    height: 425px;
    background: var(--card);
    overflow: hidden;
  }
  .card--front { top: 119px; }
  .card--back { top: 635px; }

  .front-accent {
    position: absolute;
    left: 0;
    top: 0;
  }

  .contact-block {
    position: absolute;
    left: 36px;
    top: 196px;
  }
  .person-name {
    font-size: 31px;
    color: var(--name);
    line-height: 1;
    margin-bottom: 14px;
  }
  .person-role {
    font-size: 21px;
    line-height: 29px;
    color: var(--teal);
    margin-bottom: 14px;
  }
  .contact-line {
    font-size: 20.5px;
    line-height: 31px;
    color: var(--ink);
  }

  .brand {
    position: absolute;
    left: 0;
    right: 0;
    top: 148px;
    text-align: center;
  }
  .brand-dot {
    display: block;
    width: 46px;
    height: 46px;
    margin: 0 auto 22px;
    border-radius: 50%;
    background: var(--teal);
  }
  .brand-name {
    font-size: 34px;
    letter-spacing: 1px;
    text-transform: uppercase;
    color: var(--brand-grey);
    line-height: 1;
  }
</style>
</head>
<body>
  <main class="canvas">
    <section class="card card--front">
      <svg class="front-accent" width="746" height="425" viewBox="0 0 746 425" aria-hidden="true">
        <circle cx="640" cy="20" r="200" fill="var(--teal)"/>
      </svg>
      <div class="contact-block">
        <h1 class="person-name">Tamsin Varga</h1>
        <p class="person-role">Personal Development<br>Coach &amp; Trainer</p>
        <p class="contact-line">+61 (0)452 819 407</p>
        <p class="contact-line">tamsin@bright-harbour.com</p>
        <p class="contact-line">www.bright-harbour.com</p>
      </div>
    </section>

    <section class="card card--back">
      <div class="brand">
        <span class="brand-dot"></span>
        <p class="brand-name">Bright Harbour Coaching</p>
      </div>
    </section>
  </main>
</body>
</html>
```